Cool date project and tattoo

My children were born randomly on dates with a crazy number sequence and I am getting married on the next date in the sequence. The dates are as follows:

6/13/14
7/15/16
8/17/18
9/19/20.

I want a piece of art that has these dates beautifully drawn/written which I also would like to turn into a tattoo one day. I am not sure whether to add the kids names or not but would also be interested in seeing options. Here are the names of the kids and the wedding:

6/13/14 - Brenno
7/15/16 - Fenna
8/17/18 - Orlith
9/19/20 - Wedding

I'd love to see options of how these dates could be presented in a unique and beautiful way!

I have not seen anything that I love yet..

Serif
Decorative
Script

• My project must have the dates included in the design
• I want to be able to see the dates relatively clearly, I want it to be able to not only be a large art project when printed on a large canvas, but also a cool looking tattoo.

Please check the color palates I added to see colors I like together.

```html
<!DOCTYPE html>
<html lang="en">
<head>
<meta charset="utf-8">
<title>Brenno Fenna Orlith Wedding – Date Sequence</title>
<link rel="stylesheet" href="https://fonts.googleapis.com/css2?family=Playfair+Display:wght@400;500&family=Cinzel+Decorative:wght@400&family=Cormorant+Garamond:wght@500&display=swap">
<style>
  :root {
    --paper: #ffffff;
    --ink: #0a0a0a;
    --ornament-tone: #d9d9d9;
  }
  html, body {
    margin: 0;
    padding: 0;
    width: 1200px;
    height: 1200px;
    overflow: hidden;
    background: var(--paper);
  }
  .artboard {
    position: relative;
    width: 1200px;
    height: 1200px;
    box-sizing: border-box;
    border: 1px solid var(--ink);
    background: var(--paper);
  }
  .artboard svg { display: block; }
  .name-initial {
    font-family: "Playfair Display", serif;
    font-weight: 500;
    font-size: 168px;
    fill: var(--ink);
  }
  .name-rest {
    font-family: "Cinzel Decorative", serif;
    font-weight: 400;
    font-size: 82px;
    fill: var(--ink);
  }
  .date {
    font-family: "Cormorant Garamond", serif;
    font-weight: 500;
    font-size: 50px;
    font-variant-numeric: lining-nums;
    fill: var(--ink);
  }
  .ornament { fill: var(--ornament-tone); }
  .footer-band { fill: var(--ink); }
</style>
</head>
<body>
<main class="artboard">
  <svg width="1198" height="1198" viewBox="0 0 1198 1198" xmlns="http://www.w3.org/2000/svg">
    <ellipse class="ornament ornament-flower" role="img" aria-label="Line-drawn flower with leaves and buds" cx="605" cy="305" rx="84" ry="58"/>

    <g class="entry entry-brenno">
      <text class="name-initial" x="224" y="492" textLength="82" lengthAdjust="spacingAndGlyphs">B</text>
      <text class="name-rest" x="318" y="442" textLength="226" lengthAdjust="spacingAndGlyphs">renno</text>
      <text class="date" x="392" y="492" textLength="152" lengthAdjust="spacingAndGlyphs">06-13-14</text>
    </g>

    <g class="entry entry-fenna">
      <text class="name-initial" x="594" y="493" textLength="100" lengthAdjust="spacingAndGlyphs">F</text>
      <text class="name-rest" x="708" y="442" textLength="266" lengthAdjust="spacingAndGlyphs">enna</text>
      <text class="date" x="826" y="492" textLength="149" lengthAdjust="spacingAndGlyphs">07-15-16</text>
    </g>

    <g class="entry entry-orlith">
      <text class="name-initial" x="124" y="659" textLength="118" lengthAdjust="spacingAndGlyphs">O</text>
      <text class="name-rest" x="248" y="606" textLength="212" lengthAdjust="spacingAndGlyphs">rlith</text>
      <text class="date" x="308" y="659" textLength="152" lengthAdjust="spacingAndGlyphs">08-17-18</text>
    </g>

    <g class="entry entry-wedding">
      <text class="name-initial" x="545" y="667" textLength="165" lengthAdjust="spacingAndGlyphs">W</text>
      <text class="name-rest" x="716" y="621" textLength="362" lengthAdjust="spacingAndGlyphs">edding</text>
      <text class="date" x="848" y="667" textLength="162" lengthAdjust="spacingAndGlyphs">09-19-20</text>
    </g>

    <ellipse class="ornament ornament-sprig" role="img" aria-label="Line-drawn leafy branch" cx="600" cy="752" rx="148" ry="54"/>

    <rect class="footer-band" x="0" y="1172" width="1198" height="26"/>
  </svg>
</main>
</body>
</html>
```